Regional beer Valmo-Bräu needs new labels for 33cl Beercans

We are looking for a creative and professional design for our 33cl beer can label. The can itself is all black, and the design should be mainly in yellow and black colors to stand out on the store shelf.
The size of the label should be 206 mm x 80 mm

*Details and requirements:*

1. brand identity and target group
- Our brand stands for handcrafted quality with a modern touch.
- The target group is young adults and beer connoisseurs who value unique taste and stylish design.

2. style and aesthetics:*
- The design should be modern and eye-catching, inspired by the labels of Kelpe Brauhaus Hamburg.
- We prefer a minimalist style with clean lines and contrasts.

3. typography:*
- Use modern, legible fonts.
- Use freely available fonts.
- The brand name and important information should be emphasized.

4. images and graphics
- The logo can be used in its entirety or in individual parts.
- Illustrations or icons that emphasize the uniqueness of our beer are welcome.

5 *Colors:*
- Main colors are yellow and black.
- Accents in other colors are possible, but should be used sparingly.

6th *Legal requirements:*
- The label must provide space for legal information such as alcohol content, origin and barcode.

7 *Technical details
- Final files should be in AI, afdesign or PDF format with a resolution of at least 300 dpi.
- The design should be created in CMYK color model.

8th *Inspiration and references:*
- Examples of labels that we like are those of Kelpe Brauhaus Hamburg. We like their clear structure and modern look.

9 *Additional information:*
- The bottling date is printed on the can or bottle afterwards.
- Special features of our beer, such as flavor or special ingredients, should be highlighted.

We look forward to your creative suggestions and hope that you will help us to design a label that perfectly represents our brand!

The target group is young adults and beer connoisseurs who value unique taste and stylish design.

Beverage

Designer to choose colors to be used in the design.

• The design should be modern and eye-catching but minimalist style with clean lines and contrasts. should include the writing valmo-bräu (attachment)

```html
<!DOCTYPE html>
<html lang="de">
<head>
<meta charset="utf-8">
<title>Valmo-Bräu Helles – Dosenetikett 33cl</title>
<link rel="stylesheet" href="https://fonts.googleapis.com/css2?family=Alfa+Slab+One&family=Oswald:wght@700&family=Arimo:wght@700&display=swap">
<style>
  :root {
    --stage: #eeeced;
    --label-black: #050505;
    --badge-black: #1c1c1c;
    --gold: #f2b300;
    --gold-deep: #c98b00;
    --glow: #ffc400;
    --cream: #fffbea;
    --ink: #111111;
    --white: #ffffff;
  }
  html, body {
    margin: 0;
    width: 1200px;
    height: 800px;
    overflow: hidden;
    background: var(--stage);
  }
  .canvas {
    position: relative;
    width: 1200px;
    height: 800px;
  }
  .can-label {
    position: absolute;
    left: 400px;
    top: 48px;
    width: 400px;
    height: 704px;
    background: var(--label-black);
  }
  .can-label svg {
    display: block;
    width: 400px;
    height: 704px;
  }
  .style-name {
    font-family: "Alfa Slab One", Georgia, serif;
    font-size: 46px;
    fill: var(--ink);
  }
  .brand-name {
    font-family: "Oswald", "Arial Narrow", sans-serif;
    font-weight: 700;
    font-size: 54px;
    fill: var(--white);
  }
  .legal-info {
    font-family: "Arimo", Arial, sans-serif;
    font-weight: 700;
    fill: var(--white);
  }
  .legal-info .abv { font-size: 13px; }
  .legal-info .volume { font-size: 16px; }
</style>
</head>
<body>
<main class="canvas">
  <section class="can-label" aria-label="Valmo-Bräu Helles Etikett">
    <svg viewBox="0 0 400 704" xmlns="http://www.w3.org/2000/svg">
      <defs>
        <linearGradient id="panel-fill" x1="0" y1="0" x2="0" y2="1">
          <stop offset="0" stop-color="#fffdf2"/>
          <stop offset="0.45" stop-color="#fff3c4"/>
          <stop offset="0.75" stop-color="#f7d36a"/>
          <stop offset="1" stop-color="#e9b21a"/>
        </linearGradient>
        <linearGradient id="hop-fill" x1="0" y1="0" x2="0" y2="1">
          <stop offset="0" stop-color="#f0b800"/>
          <stop offset="1" stop-color="#c98b00"/>
        </linearGradient>
        <filter id="soft-glow" x="-30%" y="-30%" width="160%" height="160%">
          <feGaussianBlur stdDeviation="12"/>
        </filter>
      </defs>

      <g class="glass-panel">
        <path d="M84 52 H309 Q329 52 329 72 C329 200 316 300 316 360 V624 Q316 644 296 644 H97 Q77 644 77 624 V360 C77 300 64 200 64 72 Q64 52 84 52 Z"
              fill="var(--glow)" filter="url(#soft-glow)" opacity="0.9"/>
        <path d="M84 52 H309 Q329 52 329 72 C329 200 316 300 316 360 V624 Q316 644 296 644 H97 Q77 644 77 624 V360 C77 300 64 200 64 72 Q64 52 84 52 Z"
              fill="url(#panel-fill)" stroke="var(--gold)" stroke-width="2"/>
      </g>

      <text class="style-name" x="200" y="106" text-anchor="middle">HELLES</text>

      <g class="brand-badge">
        <circle cx="200" cy="282" r="146" fill="var(--glow)" filter="url(#soft-glow)" opacity="0.85"/>
        <circle cx="200" cy="282" r="142" fill="var(--badge-black)" stroke="var(--gold)" stroke-width="4"/>
        <text class="brand-name" x="200" y="304" text-anchor="middle"
              textLength="240" lengthAdjust="spacingAndGlyphs">VALMO-BRÄU</text>
      </g>

      <rect class="hop-art" x="138" y="440" width="126" height="190" rx="44"
            fill="url(#hop-fill)" role="img"
            aria-label="Hopfendolde in Gold und Schwarz mit geschwungener Linienverzierung"/>

      <text class="legal-info" x="363" y="683" text-anchor="end">
        <tspan class="abv">Alc. 4.8% vol.</tspan>
        <tspan class="volume" dx="6">33cl</tspan>
      </text>
    </svg>
  </section>
</main>
</body>
</html>
```